Bluebrook Irrigation Business Card and Stationary
Business Cards, Envelopes, Stationary, etc.
Simple
Doug Harlan
General Operations Manager
742 Orchard Lane
Irving, TX 75119
doug@irrigatepros.com
www.irrigatepros.com
Li 48391
I want the inside part to list services that we perform.
1. Lawn Sprinkler Repair
2. Lawn Sprinkler Installation
3. Sprinkler System Efficiency Evaluation
4. French/Area Drains
5. Outdoor Lighting
6. Tree/Shrub Planting
7. Landscaping
8. Water Features
9. Sod
10. Backflow Testing
11. Outdoor/Landscape Lighting
12. Soil Test/Analysis
Arrange all of the information as you feel it fits best. I am also getting a PO box today, so the address will e different. I will update that when I have the info. Also, I would like a sticker that we can put on the customers controllers, about business card size that says "call for service," and then has our phone #. I am not opposed to having perfectly rectangular business cards, but am also not sold on it, maybe something with rounded corners.

```html
<!DOCTYPE html>
<html lang="en">
<head>
<meta charset="utf-8">
<title>Bluebrook Irrigation – Business Card</title>
<link rel="stylesheet" href="https://fonts.googleapis.com/css2?family=Arimo:wght@400;700&display=swap">
<style>
  :root {
    --stage: #e9e9ec;
    --card: #ffffff;
    --card-shade: #eef1f5;
    --band-dark: #1a2a8c;
    --band-light: #3d7fd9;
    --brand-blue: #1f6fd0;
    --text-blue: #2a86d4;
    --grass: #6bb52a;
    --muted: #6d7380;
    --rule: #c9ccd3;
  }
  * { box-sizing: border-box; margin: 0; padding: 0; }
  html, body { width: 1200px; height: 799px; overflow: hidden; }
  body {
    background: var(--stage);
    font-family: "Arimo", Arial, sans-serif;
    position: relative;
  }
  .card {
    position: absolute;
    background: radial-gradient(ellipse at 40% 45%, var(--card) 40%, var(--card-shade) 100%);
    overflow: hidden;
    box-shadow: 0 2px 6px rgba(0,0,0,.18);
  }
  .band {
    position: absolute; left: 0; right: 0;
    background: linear-gradient(90deg, var(--band-dark) 0%, var(--band-light) 50%, var(--band-dark) 100%);
  }
  .band--top { top: 0; height: 18px; }
  .band--bottom { bottom: 0; height: 24px; }

  /* Outer card: back and front */
  .card--back { left: 36px; top: 96px; width: 521px; height: 283px; }
  .card--front { left: 36px; top: 384px; width: 521px; height: 305px; }

  .back-content {
    position: absolute; inset: 0;
    transform: rotate(180deg);
  }
  .back-contact {
    position: absolute; left: 22px; top: 206px;
    font-style: normal;
    font-size: 9.5px; line-height: 15px; color: var(--muted);
    white-space: nowrap;
  }
  .back-mark {
    position: absolute; left: 20px; top: 60px;
    display: flex; flex-direction: column; align-items: center; gap: 12px;
  }
  .brand-dot {
    width: 18px; height: 18px; border-radius: 50%;
    background: var(--brand-blue);
  }
  .back-mark .brand-dot { width: 40px; height: 40px; }
  .brand-name {
    font-weight: 700; color: var(--brand-blue);
    font-size: 24px; letter-spacing: .5px; white-space: nowrap;
  }

  .front-mark {
    position: absolute; left: 0; right: 0; top: 95px;
    display: flex; flex-direction: column; align-items: center;
  }
  .front-mark .brand-dot { width: 30px; height: 30px; margin-bottom: 12px; }
  .front-mark .brand-name { font-size: 26px; }
  .tagline {
    margin-top: 6px; font-size: 7px; font-weight: 700;
    color: var(--grass); letter-spacing: .4px;
  }
  .since { margin-top: 4px; font-size: 10px; font-weight: 700; color: var(--brand-blue); }
  .license { margin-top: 2px; font-size: 7px; color: var(--grass); }
  .person { position: absolute; left: 17px; top: 226px; }
  .person-name { font-size: 14px; color: var(--text-blue); }
  .person-title { font-size: 7px; color: var(--muted); margin-top: 2px; }
  .license-corner {
    position: absolute; right: 30px; top: 232px;
    font-size: 10px; color: var(--text-blue);
  }

  /* Inner sheet: services */
  .card--inner { left: 643px; top: 96px; width: 521px; height: 593px; }
  .inner-fold {
    position: absolute; left: 0; right: 0; top: 290px; height: 1px;
    background: var(--rule);
  }
  .services { position: absolute; left: 36px; list-style: none; }
  .services--top { top: 28px; }
  .services--bottom { top: 302px; }
  .service {
    display: flex; align-items: center; gap: 12px;
    height: 42px; font-size: 14px; color: var(--text-blue);
  }
  .service svg { flex: none; }
</style>
</head>
<body>

<section class="card card--back" aria-label="Card back">
  <div class="back-content">
    <div class="band band--top"></div>
    <div class="band band--bottom"></div>
    <div class="back-mark">
      <span class="brand-dot"></span>
      <span class="brand-name">Bluebrook Irrigation</span>
    </div>
    <address class="back-contact">
      742 Orchard Lane · Irving, TX 75119<br>
      Ph.: 972-555-0148 Cell: 972-555-0193 Fax: 972-555-0148<br>
      Email: doug@irrigatepros.com · Web: www.irrigatepros.com
    </address>
  </div>
</section>

<section class="card card--front" aria-label="Card front">
  <div class="band band--top"></div>
  <div class="band band--bottom"></div>
  <div class="front-mark">
    <span class="brand-dot"></span>
    <span class="brand-name">Bluebrook Irrigation</span>
    <span class="tagline">PROVIDING QUALITY LAWN SPRINKLER SOLUTIONS TO DFW</span>
    <span class="since">SINCE 1985</span>
    <span class="license">Li 48391</span>
  </div>
  <div class="person">
    <div class="person-name">Doug Harlan</div>
    <div class="person-title">General Operations Manager</div>
  </div>
  <div class="license-corner">Li 48391</div>
</section>

<section class="card card--inner" aria-label="Card inside: services">
  <div class="band band--top"></div>
  <div class="band band--bottom"></div>
  <div class="inner-fold"></div>
  <ul class="services services--top">
    <li class="service"><svg width="9" height="9"><circle cx="4.5" cy="4.5" r="4" fill="var(--text-blue)"/></svg>Lawn Sprinkler Repair</li>
    <li class="service"><svg width="9" height="9"><circle cx="4.5" cy="4.5" r="4" fill="var(--text-blue)"/></svg>Lawn Sprinkler Installation</li>
    <li class="service"><svg width="9" height="9"><circle cx="4.5" cy="4.5" r="4" fill="var(--text-blue)"/></svg>Sprinkler System Efficiency Evaluation</li>
    <li class="service"><svg width="9" height="9"><circle cx="4.5" cy="4.5" r="4" fill="var(--text-blue)"/></svg>French/Area Drains</li>
    <li class="service"><svg width="9" height="9"><circle cx="4.5" cy="4.5" r="4" fill="var(--text-blue)"/></svg>Outdoor Lighting</li>
    <li class="service"><svg width="9" height="9"><circle cx="4.5" cy="4.5" r="4" fill="var(--text-blue)"/></svg>Tree/Shrub Planting</li>
  </ul>
  <ul class="services services--bottom">
    <li class="service"><svg width="9" height="9"><circle cx="4.5" cy="4.5" r="4" fill="var(--text-blue)"/></svg>Landscaping</li>
    <li class="service"><svg width="9" height="9"><circle cx="4.5" cy="4.5" r="4" fill="var(--text-blue)"/></svg>Water Features</li>
    <li class="service"><svg width="9" height="9"><circle cx="4.5" cy="4.5" r="4" fill="var(--text-blue)"/></svg>Sod</li>
    <li class="service"><svg width="9" height="9"><circle cx="4.5" cy="4.5" r="4" fill="var(--text-blue)"/></svg>Backflow Testing</li>
    <li class="service"><svg width="9" height="9"><circle cx="4.5" cy="4.5" r="4" fill="var(--text-blue)"/></svg>Outdoor/Landscape Lighting</li>
    <li class="service"><svg width="9" height="9"><circle cx="4.5" cy="4.5" r="4" fill="var(--text-blue)"/></svg>Soil Test/Analysis</li>
  </ul>
</section>

</body>
</html>
```